Business card to be used as a flyer

This business card should do the trick of a full scale flyer , so basicaly from the business card itself we only keep the size and remove the clasical name , position , company name (etc).
This business cards should be , like said above, used as promo tool, being gived to different girls . So base one : the design is girls oriented.
Colors : black background . We will use gold (color) folio for the text.
Attached you have our logo, but this should not be a proiminent part of the design . You can use only the cat head instead.
Target Market(s)
Girls / Women
Contact Information for Business Card
> black background , gold / folio text and elements
> cat head from the logo in a creative way do be displayed
> proieminent text "your path to success starts here"
> contact details phone and website .
www.velvadrome.ro (website) and 0741263519 (phone)
Font styles to use
Colors
Designer to choose only greyscale colors for use in the design.
Look and feel

```html
<!DOCTYPE html>
<html lang="en">
<head>
<meta charset="UTF-8">
<title>Velvadrome – Your path to Success Starts here</title>
<link rel="stylesheet" href="https://fonts.googleapis.com/css2?family=Great+Vibes&family=Montserrat:wght@400&display=swap">
<style>
  :root {
    --ink: #000000;
    --gold-deep: #8a6420;
    --gold-mid: #c99a34;
    --gold-bright: #f3d46a;
    --gold-pale: #fbe9a2;
    --gold-text: #f1e4c0;
    --glow: rgba(196, 150, 52, 0.22);
  }
  * { margin: 0; padding: 0; box-sizing: border-box; }
  html, body {
    width: 1200px;
    height: 686px;
    overflow: hidden;
    background: var(--ink);
  }
  .card {
    position: relative;
    width: 1200px;
    height: 686px;
    background: var(--ink);
    overflow: hidden;
  }
  .emblem-area {
    position: absolute;
    left: 250px;
    top: 0;
    width: 780px;
    height: 686px;
    background: radial-gradient(ellipse 50% 55% at 55% 40%, var(--glow) 0%, rgba(196,150,52,0.08) 55%, rgba(0,0,0,0) 100%);
  }
  .headline {
    position: absolute;
    left: 0;
    width: 100%;
    text-align: center;
    font-family: "Great Vibes", cursive;
    font-weight: 400;
    line-height: 1;
    background: linear-gradient(100deg, var(--gold-deep) 0%, var(--gold-bright) 22%, var(--gold-mid) 45%, var(--gold-pale) 62%, var(--gold-mid) 80%, var(--gold-bright) 100%);
    -webkit-background-clip: text;
    background-clip: text;
    color: transparent;
  }
  .headline--lead {
    top: 118px;
    padding-left: 22px;
    font-size: 118px;
  }
  .headline--main {
    top: 240px;
    padding-left: 40px;
    font-size: 158px;
  }
  .contacts {
    position: absolute;
    top: 447px;
    left: 311px;
    display: flex;
    gap: 74px;
    align-items: center;
  }
  .contact {
    display: flex;
    align-items: center;
    gap: 10px;
    font-family: "Montserrat", sans-serif;
    font-size: 24px;
    color: var(--gold-text);
    letter-spacing: 0.2px;
  }
  .contact__icon {
    width: 40px;
    height: 40px;
    flex: none;
  }
</style>
</head>
<body>
  <main class="card">
    <div class="emblem-area" role="img" aria-label="Large decorative gold emblem behind the headline"></div>

    <h1 class="headline headline--lead">Your path to</h1>
    <p class="headline headline--main">Success Starts here</p>

    <div class="contacts">
      <div class="contact contact--phone">
        <svg class="contact__icon" viewBox="0 0 40 40" aria-hidden="true">
          <defs>
            <linearGradient id="iconGold" x1="0" y1="0" x2="1" y2="1">
              <stop offset="0" stop-color="#f3d46a"/>
              <stop offset="0.5" stop-color="#c99a34"/>
              <stop offset="1" stop-color="#f3d46a"/>
            </linearGradient>
          </defs>
          <rect x="2" y="2" width="36" height="36" rx="7" fill="none" stroke="url(#iconGold)" stroke-width="2.2"/>
          <path d="M14 11 l4 0 l1.5 5 l-2.5 2 a12 12 0 0 0 5 5 l2 -2.5 l5 1.5 l0 4 a2 2 0 0 1 -2 2 a17 17 0 0 1 -15 -15 a2 2 0 0 1 2 -2 z" fill="none" stroke="url(#iconGold)" stroke-width="2" stroke-linejoin="round"/>
        </svg>
        <span class="contact__text">0741263519</span>
      </div>
      <div class="contact contact--web">
        <svg class="contact__icon" viewBox="0 0 40 40" aria-hidden="true">
          <rect x="2" y="2" width="36" height="36" rx="7" fill="none" stroke="url(#iconGold)" stroke-width="2.2"/>
          <g fill="none" stroke="url(#iconGold)" stroke-width="1.8">
            <circle cx="20" cy="20" r="10"/>
            <ellipse cx="20" cy="20" rx="4.5" ry="10"/>
            <line x1="10" y1="20" x2="30" y2="20"/>
            <path d="M12 14.5 h16 M12 25.5 h16"/>
          </g>
        </svg>
        <span class="contact__text">www.velvadrome.ro</span>
      </div>
    </div>
  </main>
</body>
</html>
```